Double-Gate-Fold Mailer (8-panels)

I have an 8-panel brochure/mailer that I need designed. We're looking for something very classy and professional-looking (both in the fonts and the imagery chosen), as this is for a medical educational event for doctors - and our members are very discerning.

We're open to any design idea that fits within the parameters given below, but if it helps, our primary color is PMS 295 (Hex #002e5a) and we often use PMS 452 (Hex #aaa77e) as a contrasting color.

Images using the NYC skyline or major landmarks are fine, as this will be held in NYC again this year. I have attached photos of the venues that could be used as pop-out images, faded background images or for other inspiration. (I do not have higher-resolution versions of any of the venue photos.)

More info about this event can be found here: http://brelvanguild.org/2017annualmtg/

Important Notes:

- This year's mailer needs to be 20.75" x 8.75” (flat), which will be folded down to 5.19" x 8.75" ultimately.

- I will provide final text for designer, but I have attached last year's mailer so that you can use the content from this as placeholder text. Latin text is also fine - just looking for the design right now.

- *** This year's mailer WILL NOT HAVE a registration form, so please don't include the registration form portion in your design. *** We have, however, added an extra session this year (the day before), so the extra space could be used to promote this new 4-hour event.

- In case it matters to your design, the two events will be in two different locations.

- Final deliverable must include raw files, including main project file (either .ai, .idml, or psd format) and fonts, images, etc.
Updates

Project Deadline Extended Reason: While there are a couple that are interesting and some that are close to our in-house style and tone, I haven't yet seen an outstanding entry (one that followed the directions) yet, especially with respect to subtle/minimal imagery. I would like to give it a few more days. Added Wednesday, July 19, 2017

Target Market(s)

Physicians, nurses, technologists (Please do not use stock images of physicians, nurses, etc. This is a direct-mail brochure; they will know it is for them.)

Industry/Entity Type

Education

Font styles to use
Serif
Sans Serif

Colors

Designer to choose colors to be used in the design.

Requirements
Must have
• Must have room for all content to fit. Last year's brochure is attached as an example of the amount of content there will be. I have attached the five (5) logos that will (eventually) need to be on the brochure. They can be added later either in full color or monotone.
• This year doesn't have a theme like last year. The title of the event is simply: "The 89th Annual Scientific Session & Inaugural PQR Quillbox Challenge"
Nice to have
• Nice to have a design that somehow coordinates with our logos, which, as you can see, range in color from dark blue to light blue, but this isn't necessary, as our logos can all be monotone if necessary. It would be nice if the designer could keep the horizontal-style of the art, similar to last year's, but it's not a requirement.
Should not have
• Images should be subtle, faded or pushed to the background. Please don't include stock images of people, physicians working, medical equipment, etc. (This is a highly specialized field of medicine, and generic stock images look very strange and, at best, are a misrepresentation of these doctors.) Art should not be to "cartoon-y" either or have too many distracting images.

```html
<!DOCTYPE html>
<html lang="en">
<head>
<meta charset="utf-8">
<title>89th Annual Scientific Session – Mailer</title>
<link rel="stylesheet" href="https://fonts.googleapis.com/css2?family=Noto+Serif:ital,wght@0,400;0,700;1,400&family=Cormorant+SC:wght@400;500&family=Open+Sans:wght@400;700&display=swap">
<style>
:root{
  --page:#eeeeee;
  --panel-grey:#f1f2f3;
  --cover-blue:#1a6792;
  --cover-deep:#0d4d73;
  --heading-blue:#2a6ea0;
  --title-light:#b9d0de;
  --ink:#1b1b1b;
  --inside-blue:#21628a;
  --inside-band:#2c5775;
  --promo-blue:#1f6b97;
  --promo-text:#55b6cc;
  --label:#9bbcd0;
  --box:#d9eaf2;
  --box-strip:#a8dcdc;
  --box-strip-deep:#2b94b8;
  --box-ink:#3c4a55;
  --link:#2d5f88;
  --map-water:#2f6a8c;
  --map-land:#59b3cc;
}
*{box-sizing:border-box;margin:0;padding:0}
html,body{width:1200px;height:1013px;overflow:hidden;background:var(--page)}
.sheet{position:absolute;left:40px;width:985px;height:415px;transform:scale(1.137);transform-origin:0 0;overflow:hidden;box-shadow:0 2px 6px rgba(0,0,0,.18)}
.sheet--outside{top:24px}
.sheet--inside{top:517px;background:var(--inside-blue)}
.abs{position:absolute}

/* outside */
.panel-grey{background:linear-gradient(180deg,#f7f7f7 0%,#e6e8ea 55%,#f3f3f3 100%)}
.skyline-faint{position:absolute;left:0;right:0;top:110px;height:230px;background:linear-gradient(180deg,rgba(200,205,210,0) 0%,rgba(190,196,202,.45) 45%,rgba(215,220,224,.3) 100%)}
.section-head{font:italic 400 8.5px/1 "Noto Serif",serif;color:var(--heading-blue)}
.body-serif{font:400 5.4px/1.28 "Noto Serif",serif;color:var(--ink);text-align:justify}
.body-serif p{margin-bottom:6px}
.cover-photo{left:245px;top:0;width:493px;height:415px;background:linear-gradient(180deg,#2b79a4 0%,#1d6a95 40%,#104e74 75%,#0b3f60 100%)}
.cover-intro{left:295px;top:62px;width:160px;font:italic 400 8.4px/1.35 "Noto Serif",serif;color:#fff}
.title{left:531px;top:90px;color:var(--title-light);font-family:"Cormorant SC",serif;font-weight:400}
.title-num{font-size:52px;line-height:1;letter-spacing:1px}
.title-word{font-size:20px;line-height:1.12;letter-spacing:1px}
.title-date{font-size:24px;margin-top:8px;font-family:"Noto Serif",serif;font-weight:400}
.org-mark{left:548px;top:19px;display:flex;align-items:center;gap:8px}
.org-dot{width:32px;height:32px;border-radius:50%;background:var(--cover-deep)}
.org-name{font:400 11px/1.05 "Noto Serif",serif;color:var(--cover-deep);border-left:1px solid var(--cover-deep);padding-left:6px}
.faculty{left:782px;top:68px;width:161px}
.faculty p{margin-bottom:5px}

/* inside */
.label{font:italic 400 12px/1 "Noto Serif",serif;color:var(--label)}
.info-box{background:var(--box);font:400 5.3px/1.55 "Open Sans",sans-serif;color:var(--box-ink)}
.info-box b{font-weight:700;color:#26313a}
.info-box u{color:var(--link)}
.info-box hr{border:0;border-top:1px solid #a9c3cf;margin:5px -5px}
.box-when{left:104px;top:0;width:131px;height:388px;padding:19px 5px 0}
.box-when::before{content:"";position:absolute;left:0;top:0;right:0;height:13px;background:var(--box-strip)}
.box-stay{left:342px;top:0;width:149px;height:372px;padding:14px 5px 0}
.box-stay::before{content:"";position:absolute;left:0;top:0;right:0;height:8px;background:var(--box-strip-deep)}
.box-stay ul{padding-left:9px}
.box-stay .more{position:absolute;left:5px;right:5px;top:322px}
.band{left:0;top:373px;width:645px;height:42px;background:var(--inside-band)}
.promo{left:491px;top:0;width:154px;height:373px;background:var(--promo-blue)}
.promo-text{left:518px;top:34px;width:118px;font:italic 400 8.6px/1.3 "Noto Serif",serif;color:var(--promo-text)}
.promo-text p{margin-bottom:14px}
.map{left:645px;top:0;width:340px;height:415px;background:linear-gradient(160deg,var(--map-water) 0%,#3f86a8 45%,var(--map-land) 70%,#2f6a8c 100%)}
</style>
</head>
<body>

<section class="sheet sheet--outside" aria-label="Outside spread">
  <div class="abs panel-grey" style="left:0;top:0;width:245px;height:415px">
    <div class="skyline-faint" role="img" aria-label="Faded city skyline over the water"></div>
  </div>
  <div class="abs section-head" style="left:34px;top:48px">Lorem Ipsum Dolor</div>
  <div class="abs body-serif" style="left:35px;top:76px;width:166px">Lorem ipsum dolor sit amet, consectetur adipiscing elit. Nunc et quam a metus cursus mollis quis ut eros. Orci varius natoque penatibus et magnis dis parturient montes, nascetur ridiculus mus. Proin condimentum mauris felis, eget tempor ex sodales at. Praesent quis urna magna. Duis maximus eros sollicitudin eros sagittis, nec porta elit cursus. Phasellus pulvinar in est et volutpat. Sed dignissim aliquet mollis. Mauris erat nulla, consectetur ut convallis et, rutrum et sem. Nam euismod malesuada fermentum. Morbi rutrum vehicula eros. Sed varius viverra erat eget tristique.</div>
  <div class="abs section-head" style="left:34px;top:182px">Lorem Ipsum Dolor</div>
  <div class="abs body-serif" style="left:35px;top:211px;width:166px">Lorem ipsum dolor sit amet, consectetur adipiscing elit. Nunc et quam a metus cursus mollis quis ut eros. Orci varius natoque penatibus et magnis dis parturient montes, nascetur ridiculus mus. Proin condimentum mauris felis, eget tempor ex sodales at. Praesent quis urna magna.</div>
  <div class="abs section-head" style="left:34px;top:282px">Lorem Ipsum Dolor</div>
  <div class="abs body-serif" style="left:35px;top:310px;width:166px">Lorem ipsum dolor sit amet, consectetur adipiscing elit. Nunc et quam a metus cursus mollis quis ut eros. Orci varius natoque penatibus et magnis dis parturient montes, nascetur ridiculus mus. Proin condimentum mauris felis, eget tempor ex sodales at. Praesent quis urna magna.</div>

  <div class="abs cover-photo" role="img" aria-label="Aerial view of the Manhattan skyline in a blue duotone"></div>
  <p class="abs cover-intro">Lorem ipsum dolor sit amet, consectetur adipiscing elit. Nunc et quam a metus cursus mollis quis ut eros. Orci varius natoque penatibus et magnis dis parturient montes, nascetur ridiculus mus.</p>

  <svg class="abs" style="left:0;top:0" width="985" height="70" aria-hidden="true"><polygon points="491,0 738,0 718,64 511,64" fill="#fff"/></svg>
  <div class="abs org-mark">
    <span class="org-dot"></span>
    <span class="org-name">Brelvan Guild<br>State Chapter</span>
  </div>
  <div class="abs title">
    <div class="title-num">89th</div>
    <div class="title-word">Annual</div>
    <div class="title-word">Scientific</div>
    <div class="title-word">Session</div>
    <div class="title-date">12/7/17</div>
  </div>

  <div class="abs panel-grey" style="left:738px;top:0;width:247px;height:415px">
    <div class="skyline-faint" style="top:150px" role="img" aria-label="Faded city skyline"></div>
  </div>
  <div class="abs section-head" style="left:763px;top:29px">89th Annual Scientific Session</div>
  <div class="abs body-serif faculty">
    <p>This annual event brings together cardiologists, cardio-thoracic surgeons, internists, family practitioners, gerontologists, oncologists, cardiac nurse practitioners, physician assistants, cardiology fellows in training (FITs) and all members of the cardiac care team. The event is presented by Harbor Cardiological Society, the Brelvan Guild State Chapter of the Brelvan College of Cardiology and the Harbor Cardiac Center.</p>
    <p style="margin-bottom:40px">The Annual Scientific Session also features the winners of the Annual Young Investigators' Competition, which is now open, and this year will ALSO feature the winners of the Inaugural PQR Quillbox Challenge!</p>
    <p>The faculty lineup for this year's Annual Scientific Session, alphabetically, are:</p>
    <p><b>Martin L. Ashdown</b> MD, FACC | Westvale Medical Center (Los Angeles)</p>
    <p><b>Reed P. Calloway</b> MD, FACC, FAHA | Clinical Transformation Cedarbrook Heart and Vascular Institute (Portland, OR)</p>
    <p><b>R. Hale Ormond</b>, MD, MBA, FACC | Halden Medical College (New York City)</p>
    <p><b>Tomás R. Verano</b>, MD, PhD, FACC, FSIAC, FESC | Governor, Southern Cone Chapter of the BCC (Buenos Aires, Argentina)</p>
    <p><b>Lucio B. Ferrant</b>, MD, FACC, FAHA | Rivermoor Medical Center (Valhalla, NY)</p>
    <p><b>Rubén C. Solari</b>, MD, FACC | Past President, Southern Cone Federation of Cardiology | Hospital Norte Verano (Santa Fe, Argentina)</p>
    <p><b>Clara M. Denholm</b>, MD | Lakeshore University School of Medicine (Chicago)</p>
  </div>
</section>

<section class="sheet sheet--inside" aria-label="Inside spread">
  <div class="abs label" style="left:35px;top:18px">What:</div>
  <div class="abs label" style="left:35px;top:40px">When:</div>
  <div class="abs label" style="left:35px;top:140px">Where:</div>
  <div class="abs label" style="left:45px;top:238px">Cost:</div>

  <div class="abs info-box box-when">
    89th Annual Scientific Session
    <hr>
    <b>Cocktail Reception, Whiskey Tasting &amp; Inaugural PQR Quillbox Challenge:</b> Wednesday, Dec. 6th, 2017, from 6:30 to 10:30 p.m. | Click here for more info.<br>
    <span style="display:block;height:4px"></span>
    <b>Scientific Session:</b> Thursday, Dec. 7th, 2017, from 7:30 a.m. to 3 p.m.<br>
    <span style="display:block;height:4px"></span>
    <b>Council Meeting:</b> BVG Council Members Only (Click <u>here</u> for details)
    <hr>
    <b>Cocktail Reception, Whiskey Tasting &amp; Inaugural PQR Quillbox Challenge:</b> <u>Oak &amp; Ember Hall</u>, 14 E 41st St, New York, NY 10016<br>
    <span style="display:block;height:4px"></span>
    <b>Scientific Session:</b> <u>The Linden Ballroom</u>, 22 E 29th St, NY, NY 10016<br>
    <span style="display:block;height:4px"></span>
    <b>Council Meeting:</b> BVG Council Members Only (Click <u>here</u> for details)
    <hr>
    <u>Scientific Session Early-Bird Rates (Before 10/2/2017)</u><br>
    BVG/BCC/Southern Cone Member (Physician) – $75<br>
    BVG/BCC/Southern Cone Member (CVT/Other) – $35<br>
    BVG/BCC/Southern Cone Non-Member (Physician) – $150<br>
    BVG/BCC/Southern Cone Non-Member (CVT/Other) – $70<br>
    <u>Scientific Session Regular Rates (On or After 10/2/2017)</u><br>
    BVG/BCC/Southern Cone Member (Physician) –
  </div>

  <div class="abs label" style="left:247px;top:131px">Accommodation</div>
  <div class="abs label" style="left:262px;top:322px;line-height:1.2">Additional<br>Information</div>

  <div class="abs info-box box-stay">
    BVG/BCC/Southern Cone Member (CVT/Other) – $55<br>
    BVG/BCC/Southern Cone Non-Member (Physician) – $175<br>
    BVG/BCC/Southern Cone Non-Member (CVT/Other) – $90<br>
    <span style="display:block;height:5px"></span>
    <u>Scientific Session Walk-In Rates (On 12/7/2017)</u><br>
    <span style="display:block;height:5px"></span>
    All Levels – $199
    <hr>
    Should you want a hotel closer to Oak &amp; Ember, where the prior night's <u>Cocktail Reception &amp; Quillbox Challenge</u> will be held, there are courtesy room blocks at:
    <ul>
      <li><u>The Ardent</u> (4-min. walk to Oak &amp; Ember) | Call 800-555-0142 and mention "Harbor Cardiological Society" for a rate of $309 (excl. taxes) for a room with a king-size bed<br>[Offer expires 11/08/17]</li>
      <li style="margin-top:4px"><u>The Marlow</u> (7-min. walk to Oak &amp; Ember) | Call 888-555-0176 and mention "Harbor Cardiological Society" for a rate of $259 (excl. taxes) for a room with a king-size bed<br>[Offer expires 11/07/17]</li>
    </ul>
    <div class="more">
      <hr style="margin-bottom:4px">
      For more information or to inquire about becoming an exhibitor at this year's Scientific Session, email info@brelvanguild.org or (212) 555-0119
    </div>
  </div>

  <div class="abs band"></div>
  <div class="abs promo"></div>
  <div class="abs promo-text">
    <p>Lorem ipsum dolor sit amet, consectetur adipiscing elit. Nunc et quam a metus cursus mollis quis ut eros. Orci varius natoque penatibus et magnis dis parturient montes, nascetur ridiculus mus. Proin condimentum mauris felis, eget tempor ex sodales at. Praesent quis urna magna.</p>
    <p>Duis maximus eros sollicitudin eros sagittis, nec porta elit cursus. Phasellus pulvinar in est et volutpat. Sed dignissim aliquet mollis. Mauris erat nulla, consectetur ut convallis et, rutrum et sem. Nam euismod malesuada fermentum. Morbi rutrum vehicula eros. Sed varius viverra erat eget tristique.</p>
  </div>

  <div class="abs map" role="img" aria-label="Street map of Manhattan with the Hudson and East Rivers, New Jersey, Queens and Brooklyn, and venue markers"></div>
</section>

</body>
</html>
```